Business Card Design

I am a Building Surveyor and run my own Building Consultat company, providing professional advice and services to builders, architects, designers, owners, etc.

Industry/Entity Type

Business

Contact Information for Business Card

Dorwen Fasque BBldgSurv (Hons)
Managing Director

47 Marlow Crest, Kelvoth Downs WA 6158
Mobile 0498 153 607
Email Dorwen.fasque@ridgeplumbav.com

Requirements
Must have
• I would like the back of the business card to be one colour (a shade of either black or maroon, matching the colours of my logo). Positioned in the centre on the back of the business card is to be my logo.

The front of the card is to be white, with my contact information in either black or maroon. The ADBldgSurv after my name should be in a smaller font size than my name. I would also like a small logo somewhere on this side of the card.

```html
<!DOCTYPE html>
<html lang="en">
<head>
<meta charset="utf-8">
<title>Holloway Building Consultants — Business Card</title>
<link rel="stylesheet" href="https://fonts.googleapis.com/css2?family=Cinzel:wght@400;600&family=Open+Sans:wght@400;600&display=swap">
<style>
  :root {
    --maroon: #5e1c12;
    --grey: #5b5b5b;
    --rule: #9a9a9a;
    --ink: #2a2a2a;
    --white: #ffffff;
    --backdrop: #ece8e3;
  }
  * { box-sizing: border-box; margin: 0; padding: 0; }
  html, body {
    width: 1200px; height: 1024px; overflow: hidden;
    background: var(--backdrop);
  }
  .canvas {
    position: relative; width: 1200px; height: 1024px;
    display: flex; align-items: center; justify-content: center; gap: 40px;
  }
  .card {
    position: relative; width: 540px; height: 330px; overflow: hidden;
    box-shadow: 0 6px 18px rgba(0,0,0,.18);
  }
  /* Front */
  .card-front { background: var(--white); }
  .front-sweep { position: absolute; inset: 0; width: 100%; height: 100%; }
  .wordmark {
    position: absolute; left: 30px; top: 44px;
    display: flex; align-items: center; gap: 12px;
  }
  .wordmark-dot {
    width: 30px; height: 30px; border-radius: 50%;
    background: var(--maroon);
  }
  .wordmark-name {
    font-family: 'Cinzel', serif; font-weight: 400; color: var(--ink);
    font-size: 25px; line-height: 1; letter-spacing: 1px;
  }
  .wordmark-sub {
    font-family: 'Cinzel', serif; font-weight: 400; color: var(--ink);
    font-size: 8.5px; letter-spacing: 1.6px; margin-top: 4px;
    border-top: 1px solid var(--rule); padding-top: 3px; text-align: center;
  }
  .divider {
    position: absolute; left: 24px; top: 108px; width: 450px; height: 1px;
    background: var(--rule);
  }
  .person { position: absolute; left: 288px; top: 58px; }
  .person-name {
    font-family: 'Cinzel', serif; font-weight: 600; color: var(--maroon);
    font-size: 19px; letter-spacing: .5px; line-height: 1;
  }
  .person-title {
    font-family: 'Open Sans', sans-serif; color: var(--ink);
    font-size: 11px; margin-top: 8px;
  }
  .contacts {
    position: absolute; left: 30px; top: 126px; list-style: none;
    font-family: 'Open Sans', sans-serif; color: var(--ink); font-size: 12px;
  }
  .contacts li { display: flex; align-items: center; gap: 10px; height: 26px; }
  .contacts svg { width: 12px; height: 12px; fill: var(--maroon); flex: none; }
  /* Back */
  .card-back {
    background: var(--maroon);
    display: flex; align-items: center; justify-content: center;
  }
  .back-wordmark { display: flex; align-items: center; gap: 18px; color: var(--white); }
  .back-dot { width: 54px; height: 54px; border-radius: 50%; border: 3px solid var(--white); }
  .back-name {
    font-family: 'Cinzel', serif; font-weight: 400;
    font-size: 40px; letter-spacing: 2px; line-height: 1;
  }
  .back-sub {
    font-family: 'Cinzel', serif; font-weight: 400;
    font-size: 12px; letter-spacing: 3px; margin-top: 8px;
    border-top: 1px solid rgba(255,255,255,.7); padding-top: 5px; text-align: center;
  }
</style>
</head>
<body>
<main class="canvas">

  <section class="card card-front" aria-label="Card front">
    <svg class="front-sweep" viewBox="0 0 540 330" preserveAspectRatio="none" aria-hidden="true">
      <path class="sweep-grey" d="M250 330 C378 265 490 175 510 0 L540 0 L540 330 Z" fill="var(--grey)"/>
      <path class="sweep-gap" d="M235 330 C390 280 510 190 532 0 L540 0 L540 330 Z" fill="var(--white)"/>
      <path class="sweep-maroon" d="M250 330 C400 290 520 200 540 30 L540 330 Z" fill="var(--maroon)"/>
    </svg>

    <div class="wordmark">
      <span class="wordmark-dot"></span>
      <div>
        <div class="wordmark-name">Holloway</div>
        <div class="wordmark-sub">Building Consultants</div>
      </div>
    </div>

    <div class="divider"></div>

    <div class="person">
      <div class="person-name">DORWEN FASQUE</div>
      <div class="person-title">ADBldgSurv Director</div>
    </div>

    <ul class="contacts">
      <li>
        <svg viewBox="0 0 12 12" aria-hidden="true"><rect x="3" y="0" width="6" height="12" rx="1.2"/></svg>
        0498 153 607
      </li>
      <li>
        <svg viewBox="0 0 12 12" aria-hidden="true"><path d="M0 2h12v8H0z M0 2l6 5 6-5" stroke="#fff" stroke-width=".8"/></svg>
        Dorwen.fasque@ridgeplumbav.com
      </li>
      <li>
        <svg viewBox="0 0 12 12" aria-hidden="true"><path d="M6 0a4 4 0 0 1 4 4c0 3-4 8-4 8S2 7 2 4a4 4 0 0 1 4-4z"/><circle cx="6" cy="4" r="1.4" fill="#fff"/></svg>
        47 Marlow Crest, Kelvoth Downs WA 6158
      </li>
    </ul>
  </section>

  <section class="card card-back" aria-label="Card back">
    <div class="back-wordmark">
      <span class="back-dot"></span>
      <div>
        <div class="back-name">HOLLOWAY</div>
        <div class="back-sub">BUILDING CONSULTANTS</div>
      </div>
    </div>
  </section>

</main>
</body>
</html>
```